Harborline Crest Insurance Services

we are a high end insurance agency we specialize on Auto | Home | Business | Life looking for something professional and luxuries at the same time. if you guys need anything else please let me know.

Auto | Home | Business | Life must be under logo on the back with black background.

i want the back part to be black with our gold logo on it.

Target Market(s)

Auto | Home | Business | Life

Industry/Entity Type

Insurance Broker

Contact Information for Business Card

My logo is gold so a black in the back would be nice.

Font styles to use
Serif

Colors
000000

Requirements
Must have
• Big logo on the back with black background.

```html
<!DOCTYPE html>
<html lang="en">
<head>
<meta charset="UTF-8">
<title>Harborline Crest Insurance Services – Business Card</title>
<link href="https://fonts.googleapis.com/css2?family=Cinzel:wght@400;700&family=EB+Garamond:wght@400;600&display=swap" rel="stylesheet">
<style>
  :root {
    --page-bg: #d9d4cc;
    --card-black: #1d1d1d;
    --card-black-deep: #121212;
    --gold: #e8c21c;
    --gold-line: #c9a515;
    --silver: #c9c9c9;
    --text-light: #ecebe7;
    --text-muted: #a9a9a9;
  }
  * { margin: 0; padding: 0; box-sizing: border-box; }
  html, body {
    width: 1018px; height: 1200px; overflow: hidden;
    background: var(--page-bg);
  }
  .canvas {
    width: 1018px; height: 1200px;
    display: flex; flex-direction: column; align-items: center; justify-content: center;
    gap: 70px;
  }
  .card {
    position: relative;
    width: 840px; height: 480px;
    background: radial-gradient(ellipse at 35% 30%, #2a2a2a 0%, var(--card-black) 55%, var(--card-black-deep) 100%);
    box-shadow: 0 8px 24px rgba(0,0,0,0.25);
  }
  .card__frame {
    position: absolute; inset: 18px;
    border: 2px solid var(--gold-line);
  }
  /* Front */
  .front__name {
    position: absolute; left: 70px; top: 62px;
    font-family: 'Cinzel', serif; font-weight: 400;
    font-size: 34px; letter-spacing: 2px;
    color: var(--gold);
  }
  .brand {
    position: absolute;
    display: flex; align-items: center; gap: 18px;
  }
  .brand__mark {
    width: 22px; height: 22px; border-radius: 50%;
    background: var(--gold); flex: none;
  }
  .brand__name {
    font-family: 'Cinzel', serif; font-weight: 700;
    color: var(--gold); line-height: 1.1;
  }
  .front__brand { left: 250px; top: 175px; }
  .front__brand .brand__name { font-size: 34px; }
  .front__contact {
    position: absolute; right: 70px; bottom: 64px;
    text-align: right;
    font-family: 'EB Garamond', serif;
  }
  .front__line { font-size: 19px; color: var(--text-light); line-height: 1.5; }
  .front__address {
    margin-top: 22px;
    font-size: 22px; font-weight: 600; color: var(--gold);
  }
  /* Back */
  .back__brand { left: 110px; top: 150px; }
  .back__brand .brand__name { font-size: 46px; }
  .back__brand .brand__mark { width: 30px; height: 30px; }
  .back__services {
    position: absolute; left: 158px; top: 320px;
    font-family: 'EB Garamond', serif; font-variant: small-caps;
    font-size: 24px; letter-spacing: 2px;
    color: var(--text-muted);
  }
  .back__services .divider { color: var(--gold); margin: 0 10px; }
</style>
</head>
<body>
<main class="canvas">
  <section class="card card--front" aria-label="Card front">
    <div class="card__frame"></div>
    <p class="front__name">Daniel Mercer</p>
    <div class="brand front__brand">
      <span class="brand__mark"></span>
      <span class="brand__name">Harborline Crest</span>
    </div>
    <div class="front__contact">
      <p class="front__line">Phone: +1 555-014-2287</p>
      <p class="front__line">contact@harborlinecrest.com</p>
      <p class="front__address">2400 Harbor Ave, Bayview, California</p>
    </div>
  </section>

  <section class="card card--back" aria-label="Card back">
    <div class="card__frame"></div>
    <div class="brand back__brand">
      <span class="brand__mark"></span>
      <span class="brand__name">Harborline Crest<br>Insurance Services</span>
    </div>
    <p class="back__services">Auto<span class="divider">|</span>Home<span class="divider">|</span>Business<span class="divider">|</span>Life</p>
  </section>
</main>
</body>
</html>
```